Web Design Project for Film Business

We need a web design for a new company based in Bondi Beach, Sydney, Australia. We basically provide filming and video editing services. Our targets are basically corporate videos, wedding videos and other types of functions.
The important thing to know about us is that we are not just people that press the record button, we consider ourselves story tellers. We can make something boring like a conference look interesting to watch and we can also make a wedding look like a blockbuster movie that you can't look away from until its finished.
We need something as new and fresh as Bondi Beach. A young place where people come from all over the world to enjoy summer and we are lucky to be based here.
To see some of our work please visit our clipnest Channel. Make sure you watch a couple of wedding video and the corporate video so you can have a better understanding about our style.
Please note- we are not trying to market ourselves exclusively as wedding videographers, nor do we want to exploit the idea of the beach.

http://clipnest.example/channels/518374

sites that we really like:

http://www.quillharbour.example.co.uk/
http://www.fennwixley.example.co.uk/

Target Market(s)

Couples - Corporate

Industry/Entity Type

Business

Requirements
Must have
• 5 to 6 pages (we are still deciding)
-main page
-our story (story about Tarrow Films)
-your story (page designated for wedding videos)
-your business (page designated for corporate videos)
-contact us
-other stuff
Nice to have
• I would like to see some animation. Maybe you can animate our logo. Up to the designer

```html
<!DOCTYPE html>
<html lang="en">
<head>
<meta charset="utf-8">
<title>Tarrow Films</title>
<link rel="stylesheet" href="https://fonts.googleapis.com/css2?family=Arimo:ital,wght@0,400;0,700;1,400&display=swap">
<style>
:root{
  --header:#111317;
  --page:#1c2129;
  --page-light:#363c46;
  --accent:#19a8cb;
  --ink:#0b0d10;
  --white:#ffffff;
  --muted:#9aa0a8;
  --footer:#c9c9c9;
  --footer-ink:#1a1a1a;
}
*{margin:0;padding:0;box-sizing:border-box}
html,body{width:1191px;height:1200px;overflow:hidden}
body{position:relative;font-family:"Arimo",Arial,sans-serif;background:radial-gradient(ellipse 520px 360px at 470px 330px,var(--page-light),var(--page) 75%);color:var(--white)}
.site-header{position:absolute;left:0;top:0;width:1191px;height:115px;background:var(--header)}
.logo{position:absolute;left:183px;top:18px;font-weight:700;font-size:37px;line-height:39px;letter-spacing:1px;color:var(--white)}
.logo span{display:block}
.logo span+span{padding-left:8px}
.main-nav{position:absolute;left:476px;top:84px;display:flex;height:28px}
.main-nav a{display:block;padding:0 8px;font-size:11.5px;font-weight:700;color:var(--white);text-decoration:none;line-height:18px;border-left:1px solid #2c3037}
.main-nav a:first-child{border-left:none;padding-right:14px}
.nav-marker{position:absolute;left:495px;top:115px}
.new-badge{position:absolute;left:920px;top:51px;width:55px;height:25px}
.new-badge span{position:absolute;left:0;top:3px;width:52px;text-align:center;font-size:12.5px;font-weight:700;color:var(--white)}
.hero-title{position:absolute;left:197px;top:161px;font-size:55px;font-weight:700;line-height:60px}
.hero-sub{position:absolute;left:198px;top:220px;font-size:32px;line-height:41px}
.hero-text{position:absolute;left:197px;top:318px;width:375px;font-size:14px;line-height:16.4px}
.ribbon{position:absolute;display:flex;align-items:center;color:var(--ink);font-weight:700;background:var(--accent);clip-path:polygon(0 0,100% 0,95% 50%,100% 100%,0 100%)}
.hero-button{left:198px;top:410px;width:240px;height:22px;padding-left:8px;font-size:13.5px;clip-path:polygon(0 0,96% 0,100% 50%,96% 100%,0 100%)}
.hero-art{position:absolute;left:673px;top:154px;width:218px;height:310px;background:radial-gradient(ellipse at center,#4a515c,transparent 70%)}
.work{position:absolute;top:517px;width:190px}
.work-photo{height:147px;border:2px solid var(--white)}
.work-title{position:relative;margin-top:22px;height:22px;width:190px;padding-left:4px;font-size:13px;clip-path:polygon(0 0,100% 0,95% 100%,0 100%)}
.work-text{margin-top:9px;padding-left:4px;font-size:11.4px;line-height:13.7px;color:var(--muted)}
.work-text em{color:var(--accent)}
.site-footer{position:absolute;left:0;top:910px;width:1191px;height:290px;background:var(--footer);color:var(--footer-ink)}
.footer-edge{position:absolute;left:0;top:-6px}
.link-list{position:absolute;top:37px;width:200px}
.link-list h3{font-size:13.3px;font-weight:700;margin-bottom:8px}
.link-list li{list-style:none;font-size:11.4px;height:25px;padding-left:13px;position:relative}
.link-list li::before{content:"";position:absolute;left:1px;top:3px;border-left:4px solid #333;border-top:3px solid transparent;border-bottom:3px solid transparent}
.social{position:absolute;left:860px;top:24px;display:flex;gap:9px}
.social span{display:block;width:30px;height:30px;border-radius:6px;border:2px solid #eee;box-shadow:0 1px 2px rgba(0,0,0,.3)}
.copyright{left:172px;top:236px;width:191px;height:21px;padding-left:8px;font-size:10.3px;color:var(--white);clip-path:polygon(0 0,96% 0,100% 50%,96% 100%,0 100%)}
</style>
</head>
<body>
<header class="site-header">
  <div class="logo"><span>TARROW</span><span>FILMS</span></div>
  <nav class="main-nav">
    <a href="#">HOME</a><a href="#">OUR STORY</a><a href="#">YOUR STORY</a><a href="#">YOUR BUSINESS</a><a href="#">CONTACT US</a><a href="#">OTHER STUFF</a>
  </nav>
  <div class="new-badge">
    <svg width="55" height="25"><polygon points="4,0 55,0 50,19 30,19 26,25 22,19 0,19" fill="#19a8cb"/></svg>
    <span>NEW</span>
  </div>
</header>
<svg class="nav-marker" width="14" height="8"><polygon points="0,0 14,0 7,7" fill="#111317"/></svg>

<section class="hero">
  <h1 class="hero-title">Lorem ipsum</h1>
  <p class="hero-sub">Dolor sit amet, conse<br>tetuer dolor sit amet</p>
  <p class="hero-text">Adipiscing elit. Aenean commodo ligula eget dolor. Aenean massa. Aum sociis natoque penatibus et magnis dis parturient montes, nascetur ridiculus mus. Donec quam felis, ultricies nec, pellentesque eu, pretium quis.</p>
  <a class="ribbon hero-button">Aenean commodo ligul aeget</a>
  <div class="hero-art" role="img" aria-label="Line drawing of a film camera on a tripod"></div>
</section>

<section class="works">
  <article class="work" style="left:177px">
    <div class="work-photo" role="img" aria-label="Couple talking by the water at sunset" style="background:linear-gradient(160deg,#c9c8c2,#8c8a9a 55%,#4f6a7c)"></div>
    <h2 class="ribbon work-title">Maecenas nec odio et ante</h2>
    <p class="work-text">Tincidunt tempus donec vitae sapien ut libero venenatis faucibus. Nullam quis ante. Etiam sit amet orci eget eros faucibus tincidunt. Duis leo. Sed fringilla mauris sit amet nibh. Donec sodales sagittis magna. Sed consequat, leo eget bibendum sodales, augue velit cursus <em>Read More...</em></p>
  </article>
  <article class="work" style="left:389px">
    <div class="work-photo" role="img" aria-label="Surfer walking across a sandy beach" style="background:linear-gradient(170deg,#7a5a3c,#b58a5e 50%,#5d412a)"></div>
    <h2 class="ribbon work-title">Maecenas nec odio et ante</h2>
    <p class="work-text">Tincidunt tempus donec vitae sapien ut libero venenatis faucibus. Nullam quis ante. Etiam sit amet orci eget eros faucibus tincidunt. Duis leo. Sed fringilla mauris sit amet nibh. Donec sodales sagittis magna. Sed consequat, leo eget bibendum sodales, augue velit cursus nunc <em>Read More...</em></p>
  </article>
  <article class="work" style="left:603px">
    <div class="work-photo" role="img" aria-label="Close-up of hands playing an acoustic guitar" style="background:linear-gradient(120deg,#e8d4c4,#b88d6a 50%,#6a4a38)"></div>
    <h2 class="ribbon work-title">Maecenas nec odio et ante</h2>
    <p class="work-text">Tincidunt tempus donec vitae sapien ut libero venenatis faucibus. Nullam quis ante. Etiam sit amet orci eget eros faucibus tincidunt. Duis leo. Sed fringilla mauris sit amet nibh. Donec sodales sagittis magna. Sed consequat, leo eget bibendum sodales, augue velit cursus nunc<em>Read More...</em></p>
  </article>
  <article class="work" style="left:815px">
    <div class="work-photo" role="img" aria-label="Conference venue lobby with attendees" style="background:linear-gradient(90deg,#2a2c30,#4c5358 50%,#a9b6bd)"></div>
    <h2 class="ribbon work-title">Maecenas nec odio et ante</h2>
    <p class="work-text">Tincidunt tempus donec vitae sapien ut libero venenatis faucibus. Nullam quis ante. Etiam sit amet orci eget eros faucibus tincidunt. Duis leo. Sed fringilla mauris sit amet nibh. Donec sodales sagittis magna. Sed consequat, leo eget bibendum sodales, augue velit cursus nunc<em>Read More...</em></p>
  </article>
</section>

<footer class="site-footer">
  <svg class="footer-edge" width="1191" height="7"><pattern id="zig" width="8" height="7" patternUnits="userSpaceOnUse"><polygon points="0,7 4,0 8,7" fill="#c9c9c9"/></pattern><rect width="1191" height="7" fill="url(#zig)"/></svg>
  <div class="link-list" style="left:177px">
    <h3>Maecenas nec odio et ante</h3>
    <ul><li>Tincidunt tempus donec</li><li>Vitae sapien ut libero</li><li>Venenatis faucibus</li><li>Nullam quis ante</li><li>Etiam sit amet orcic</li></ul>
  </div>
  <div class="link-list" style="left:395px">
    <h3>Maecenas nec odio et ante</h3>
    <ul><li>Tincidunt tempus donec</li><li>Vitae sapien ut libero</li><li>Venenatis faucibus</li><li>Nullam quis ante</li><li>Etiam sit amet orcic</li></ul>
  </div>
  <div class="link-list" style="left:613px">
    <h3>Maecenas nec odio et ante</h3>
    <ul><li>Tincidunt tempus donec</li><li>Vitae sapien ut libero</li><li>Venenatis faucibus</li><li>Nullam quis ante</li><li>Etiam sit amet orcic</li></ul>
  </div>
  <div class="social">
    <span style="background:#3bb0e0" aria-label="Social link"></span>
    <span style="background:#3b5998" aria-label="Social link"></span>
    <span style="background:#1a8fc2" aria-label="Social link"></span>
    <span style="background:#f2f2f2" aria-label="Social link"></span>
  </div>
  <p class="ribbon copyright">© Copyright 2011 TARROW FILMS</p>
</footer>
</body>
</html>
```